Redesign Of Flower Delivery Subscription Service Website

I need a revamped website of www.petal-rush.com

Please revamp current design using same content....

Target Market(s)

people who buy flowers. Brides, wedding planners, wedding photographer, married man, boyfriend, etc.

Industry/Entity Type

Florist

Number of Pages Required

5+ page

Colors

Designer to choose colors to be used in the design.

Requirements
Must have
• I need a revamped website of www.petal-rush.com
• Please revamp current design using same content....
Nice to have
Should not have

```html
<!DOCTYPE html>
<html lang="en">
<head>
<meta charset="utf-8">
<title>Petal Rush – Monthly Flower Delivery</title>
<link href="https://fonts.googleapis.com/css2?family=Raleway:wght@400;500;600&family=Open+Sans:wght@400;600&display=swap" rel="stylesheet">
<style>
:root{
  --green:#8cc63f;
  --green-dark:#76ad2e;
  --charcoal:#4a4a4a;
  --charcoal-deep:#3f3f3f;
  --ink:#333;
  --muted:#666;
  --light:#f0f0f0;
  --white:#fff;
}
*{box-sizing:border-box;margin:0;padding:0}
html,body{width:1200px;height:3358px;overflow:hidden}
body{font-family:"Open Sans",sans-serif;color:var(--ink);background:var(--white);position:relative}
.abs{position:absolute}
h1,h2,h3,h4{font-family:"Raleway",sans-serif;font-weight:500}

/* header */
.header{top:0;left:0;width:1200px;height:125px;background:var(--white);border-bottom:1px solid #eee}
.social{top:24px;left:118px;display:flex;gap:18px}
.social span{width:14px;height:14px;border-radius:50%;background:var(--green)}
.brand{top:18px;left:0;width:1200px;text-align:center}
.brand .name{font-family:"Raleway",sans-serif;font-size:30px;font-weight:500;letter-spacing:2px;color:#555}
.brand .tag{font-size:9px;color:#777;letter-spacing:1px;margin-top:-2px}
.tools{top:24px;right:118px;display:flex;gap:22px}
.nav{top:96px;left:0;width:1200px;display:flex;justify-content:center;gap:30px;font-size:12px;font-family:"Raleway",sans-serif;color:#555}
.nav .active{color:var(--green)}

/* hero */
.hero{top:125px;left:0;width:1200px;height:520px;background:radial-gradient(circle at 60% 45%,#c76fb1 0%,#a84f8e 25%,#e6dfe8 55%,#6c8a3a 80%,#50702a 100%)}
.hero-copy{top:292px;left:90px;color:var(--white)}
.hero-copy h1{font-size:44px;font-weight:400;letter-spacing:1px}
.hero-copy p{font-size:14px;line-height:19px}
.hero-copy b{font-weight:600;font-size:15px}
.btn-green{display:inline-block;background:var(--green);color:var(--white);font-size:11px;padding:13px 38px;margin-top:34px;letter-spacing:.5px}

/* perks */
.perk{width:250px;height:250px;border-radius:50%;background:var(--charcoal);border:8px solid var(--white);display:flex;flex-direction:column;align-items:center;justify-content:center;gap:24px;color:var(--white);font-family:"Raleway",sans-serif;font-size:20px;top:540px}

/* intro */
.intro{top:868px;left:117px;width:476px}
.intro h2{font-size:28px;line-height:34px;color:var(--ink)}
.intro p{font-size:11px;line-height:15px;color:var(--muted);margin-top:16px}
.btn-dark{display:inline-block;background:var(--charcoal);color:var(--white);font-size:11px;padding:12px 22px;margin-top:28px}
.lily{top:862px;left:643px;width:557px;height:249px;background:#050505}
.lily i{position:absolute;left:240px;top:10px;width:300px;height:229px;background:radial-gradient(ellipse at center,#f7d31c 0%,#e3a80c 45%,#050505 75%)}
.rose{top:938px;left:596px;width:277px;height:288px;border:3px solid var(--white);background:radial-gradient(circle at 50% 50%,#b0285a 0%,#7a1538 40%,#0a0a0a 80%)}

/* services */
.services{top:1300px;left:0;width:1200px;height:835px;background:var(--light)}
.sec-title{left:0;width:1200px;text-align:center;font-family:"Raleway",sans-serif;font-size:26px;color:var(--ink)}
.tile{width:472px;height:308px}
.tile .label{position:absolute;bottom:14px;height:40px;background:var(--green);color:var(--white);font-family:"Raleway",sans-serif;font-size:17px;letter-spacing:.5px;display:flex;align-items:center;padding:0 32px}
.tile.left .label{left:0}
.tile.right .label{right:0}

/* how */
.video{top:2285px;left:121px;width:470px;height:270px;background:#5a5a5a;overflow:hidden}
.video .bar{position:absolute;top:0;left:0;right:0;height:36px;background:#3a3a3a;color:#eee;font-size:14px;padding:9px 56px}
.video .play{position:absolute;left:212px;top:108px;width:46px;height:46px;border-radius:50%;border:2px solid #fff;background:rgba(0,0,0,.25)}
.video .play:after{content:"";position:absolute;left:17px;top:13px;border-left:14px solid #fff;border-top:8px solid transparent;border-bottom:8px solid transparent}
.video .url{position:absolute;left:0;width:470px;text-align:center;top:172px;color:#fff;font-size:17px}
.video .cta{position:absolute;left:0;width:470px;text-align:center;top:206px;color:#fff;font-size:16px;letter-spacing:1.5px}
.video .ctrl{position:absolute;left:0;bottom:0;right:0;height:22px;background:#1c1c1c;border-top:3px solid #8a8a8a}
.how{top:2318px;left:614px;width:470px}
.how h3{font-size:27px;color:var(--ink)}
.how p{font-size:11.5px;line-height:16px;color:var(--muted);margin-top:18px}

/* newsletter */
.signup{top:2680px;left:0;width:1200px;height:355px;background:linear-gradient(180deg,#fff 0%,#f3f0ea 35%,#e9ded0 70%,#cdd6b8 100%)}
.signup .warm{position:absolute;inset:0;background:radial-gradient(circle at 88% 60%,rgba(232,90,50,.7) 0,rgba(232,90,50,0) 22%),radial-gradient(circle at 6% 55%,rgba(220,80,60,.5) 0,rgba(220,80,60,0) 14%)}
.signup h3{position:absolute;top:128px;width:1200px;text-align:center;font-size:28px;color:var(--ink)}
.field{position:absolute;top:192px;left:270px;width:500px;height:56px;background:var(--white);border:1px solid #ccc;font-size:12px;font-style:italic;color:#888;padding:19px 20px}
.submit{position:absolute;top:192px;left:770px;width:155px;height:56px;background:var(--green);color:var(--white);font-size:11px;display:flex;align-items:center;justify-content:center}

/* footer */
.footer{top:3035px;left:0;width:1200px;height:323px;background:var(--charcoal);color:var(--white)}
.col{position:absolute;top:52px}
.col h4{font-size:27px;font-weight:500;margin-bottom:14px}
.col ul{list-style:none;font-size:11px;line-height:15px}
.col li:before{content:"•";color:var(--green);margin-right:8px}
.col p{font-size:11px;line-height:14px}
.contact li:before{content:none}
.contact li{display:flex;gap:10px;margin-bottom:14px;align-items:flex-start}
.foot-social{position:absolute;top:200px;left:115px;display:flex;gap:22px}
.foot-social span{width:12px;height:12px;border-radius:50%;background:var(--green)}
.foot-social span+span{background:#888}
.rule{position:absolute;top:253px;left:115px;width:968px;height:1px;background:#6a6a6a}
.legal{position:absolute;top:272px;font-size:11px}
</style>
</head>
<body>

<header class="abs header">
  <div class="abs social"><span></span><span></span><span></span><span></span></div>
  <div class="abs brand"><div class="name">PETAL RUSH</div><div class="tag">Coastal Flower Company</div></div>
  <div class="abs tools">
    <svg width="14" height="14" viewBox="0 0 14 14"><circle cx="6" cy="6" r="4.5" fill="none" stroke="#555" stroke-width="1.6"/><path d="M9.5 9.5L13 13" stroke="#555" stroke-width="1.6"/></svg>
    <svg width="14" height="14" viewBox="0 0 14 14"><circle cx="6" cy="4" r="3" fill="none" stroke="var(--green)" stroke-width="1.5"/><path d="M1 13c0-3 2-5 5-5s5 2 5 5" fill="none" stroke="var(--green)" stroke-width="1.5"/></svg>
    <svg width="14" height="14" viewBox="0 0 14 14"><path d="M1 2h2l2 8h7l1-6H4" fill="none" stroke="var(--green)" stroke-width="1.5"/><circle cx="6" cy="12.5" r="1" fill="var(--green)"/><circle cx="11" cy="12.5" r="1" fill="var(--green)"/></svg>
  </div>
  <nav class="abs nav">
    <span class="active">Home</span><span>How it works</span><span>Delivery areas</span><span>Franchises</span><span>Corporate arrangments</span><span>Free flowers monthly</span><span>Blog</span><span>Contact</span>
  </nav>
</header>

<section class="abs hero" role="img" aria-label="Close-up bouquet of pink roses, white and purple freesias with green buds"></section>
<div class="abs hero-copy">
  <h1>ALWAYS FRESH</h1>
  <p>Beautiful Flower Arrangements Delivered Monthly<br>Now only &nbsp;<b>$69.95/MTH</b> &nbsp;&nbsp;($100 value)</p>
  <span class="btn-green">ORDER NOW &nbsp;»</span>
</div>

<div class="abs perk" style="left:156px">
  <svg width="70" height="64" viewBox="0 0 70 64"><path d="M26 4h18v8c10 4 16 12 16 22 0 14-11 26-25 26S10 48 10 34c0-10 6-18 16-22z" fill="var(--green)"/><path d="M14 34c8-4 14 4 21 0s13-4 21 0" stroke="var(--charcoal)" stroke-width="3" fill="none"/><path d="M14 44c8-4 14 4 21 0s13-4 21 0" stroke="var(--charcoal)" stroke-width="3" fill="none"/></svg>
  <span>FREE VASE</span>
</div>
<div class="abs perk" style="left:475px">
  <svg width="80" height="64" viewBox="0 0 80 64"><rect x="2" y="14" width="46" height="34" fill="var(--green)"/><path d="M48 24h16l12 12v12H48z" fill="var(--green)"/><circle cx="18" cy="52" r="7" fill="var(--green)" stroke="var(--charcoal)" stroke-width="3"/><circle cx="62" cy="52" r="7" fill="var(--green)" stroke="var(--charcoal)" stroke-width="3"/><circle cx="20" cy="28" r="10" fill="var(--charcoal)"/><path d="M20 22v7h5" stroke="var(--green)" stroke-width="2.5" fill="none"/></svg>
  <span>FREE DELIVERY</span>
</div>
<div class="abs perk" style="left:794px">
  <svg width="56" height="64" viewBox="0 0 56 64"><path d="M28 2L54 30H38v18H18V30H2z" fill="var(--green)"/><rect x="18" y="52" width="20" height="4" fill="var(--green)"/><rect x="18" y="59" width="20" height="4" fill="var(--green)"/></svg>
  <span>FREE UPGRADE</span>
</div>

<section class="abs intro">
  <h2>Monthly Subscription Based Flower Delivery Service in San Diego - CA by Our Florist Shop</h2>
  <p>Every moment of life could be cherished perfectly.......If you choose wisely. To make your day more treasured, remember that flowers are the smartest choice when delivered through our monthly PetalRush subscription based delivery service. Our online subscription-based flower delivery service can help you pamper, cherish and make an everlasting impression on the minds of your loved ones with a doorstep delivery of exquisitely hand-designed</p>
  <span class="btn-dark">READ MORE &nbsp;»</span>
</section>
<div class="abs lily" role="img" aria-label="Yellow lily in bloom on a black background"><i></i></div>
<div class="abs rose" role="img" aria-label="Deep red rose close-up on a black background"></div>

<section class="abs services">
  <h2 class="abs sec-title" style="top:63px">OUR SERVICES</h2>
  <div class="abs tile left" style="left:121px;top:114px;background:linear-gradient(135deg,#f3ecea,#e9c9cc 50%,#d9c4b6)" role="img" aria-label="Pink floral centrepieces at a draped corporate reception"><span class="label">CORPORATE ARRANGMENT</span></div>
  <div class="abs tile right" style="left:610px;top:114px;background:linear-gradient(135deg,#8a5a2e,#e8c49a 45%,#f4e6d6 70%,#c98aa0)" role="img" aria-label="Orchid arrangement in a warmly lit hotel lobby"><span class="label">HOTEL ARRANGMENT</span></div>
  <div class="abs tile left" style="left:121px;top:438px;background:linear-gradient(180deg,#d9dcdc,#f2f2f0 50%,#c9cccb)" role="img" aria-label="White flower centrepieces on banquet tables in a ballroom"><span class="label">EVENTS ARRANGMENT</span></div>
  <div class="abs tile right" style="left:610px;top:438px;background:linear-gradient(180deg,#c7cfd6,#eef0f1 45%,#b9a7b8 75%,#9c8a9a)" role="img" aria-label="Seaside wedding arch with purple flowers and rows of chairs"><span class="label">WEDDING ARRANGMENT</span></div>
</section>

<h2 class="abs sec-title" style="top:2204px">HOW IT WORKS</h2>
<div class="abs video" role="img" aria-label="Video player: subscription flower delivery explainer">
  <div class="bar">Subscription Based Flower Deli....</div>
  <div class="play"></div>
  <div class="url">PetalRushSD.com</div>
  <div class="cta">FILL OUT THE FORM ON OUR WEBSITE</div>
  <div class="ctrl"></div>
</div>
<section class="abs how">
  <h3>WATCH THE VIDEOTO LEARN MORE</h3>
  <p>PetalRush is a SET IT and FORGET IT subscription based flower delivery service. For an amazing price PetalRush will hand deliver a gorgeous arrangement directly to anyone, anywhere you want, every month.</p>
  <p>When setting up your account, Petal Rush even lets you choose exact delivery dates for your Anniversary, Birthday, Valentine's and Mother's Day.</p>
  <p>Our referral program is pretty awesome too! Just refer 3 friends and each month your 3 friends pay to have flowers delivered, your flowers will be delivered free!</p>
</section>

<section class="abs signup" role="img" aria-label="Soft field of red poppies fading into white">
  <div class="warm"></div>
  <h3>Enter Your Email To Receive A Free Upgrade</h3>
  <div class="field">Enter Your Email Address</div>
  <div class="submit">SUBMIT NOW</div>
</section>

<footer class="abs footer">
  <div class="col" style="left:115px;width:230px">
    <h4>ABOUT US</h4>
    <p>Every moment of life could be cherished perfectly.......If you choose wisely. To make your day more treasured... <span style="color:var(--green)">⊕</span></p>
  </div>
  <div class="col" style="left:420px">
    <h4>QUICK LINK</h4>
    <ul><li>Home</li><li>How it works</li><li>Delivery areas</li><li>Franchises</li><li>Corporate arrangments</li><li>Free flowers monthly</li><li>Blog</li><li>Contact</li></ul>
  </div>
  <div class="col" style="left:647px">
    <h4>SERVICES</h4>
    <ul><li>Corporate Arrangments</li><li>Hotel Arrangments</li><li>Events Arrangments</li><li>Wedding Arrangments</li></ul>
  </div>
  <div class="col contact" style="left:873px">
    <h4>QUICK LINK</h4>
    <ul>
      <li><svg width="10" height="13" viewBox="0 0 10 13"><path d="M5 0a5 5 0 015 5c0 4-5 8-5 8S0 9 0 5a5 5 0 015-5z" fill="var(--green)"/><circle cx="5" cy="5" r="2" fill="var(--charcoal)"/></svg><span>418 Harbor View Lane,<br>Bayside CA 90210</span></li>
      <li><svg width="12" height="9" viewBox="0 0 12 9"><rect width="12" height="9" fill="var(--green)"/><path d="M0 0l6 5 6-5" stroke="var(--charcoal)" fill="none"/></svg><span>support@petalrushsd.com</span></li>
      <li><svg width="11" height="11" viewBox="0 0 11 11"><path d="M2 0l2 3-1 1.5c1 1.5 2 2.5 3.5 3.5L8 7l3 2-1.5 2C5 11 0 6 0 1.5z" fill="var(--green)"/></svg><span>555-014-2290</span></li>
    </ul>
  </div>
  <div class="foot-social"><span></span><span></span><span></span><span></span></div>
  <div class="rule"></div>
  <div class="legal" style="left:115px">© Copyright 2018 Petal Rush - All Right Reserved</div>
  <div class="legal" style="right:117px">Privacy Policy - Terms &amp; Conditions</div>
</footer>

</body>
</html>
```